A Referral Pad for a Specialist Surgeon to give to referring GPs

A referral pad allows general practitioners to easily refer patients to me by quickly filling in a form on a small pad that I provide them.

A two sided referral pad themed appropriately. Theming and designing the pad should be based on the general design/logo/imagery/colours etc. from my website www.marcusbelwether.com.au. I have a logo uploaded that should be used somewhere. I have also upload a headshot of myself which might or might not be used. Other choice of imagery and design features is up to the designer.

In terms of size of the pad I’m not quite sure what is best and will leave it up to the designers.

MORE DETAILED INFORMATION IS PROVIDED IN THE UPLOADED WORD FILE

Target Market(s)

General Practitioners referring to me

Industry/Entity Type

Healthcare

Contact Information for Business Card

A business card themed as per the referral pad design as as per general look and imagery found on www.marcusbelwether.com.au

Requirements
Must have
• Referral pad details found in uploaded Word document
Nice to have
Should not have

```html
<!DOCTYPE html>
<html lang="en">
<head>
<meta charset="utf-8">
<title>Marcus Belwether – Bariatric Surgery</title>
<link href="https://fonts.googleapis.com/css2?family=Crimson+Text:wght@400;600&family=PT+Sans:wght@400&display=swap" rel="stylesheet">
<style>
  :root {
    --teal: #1a9389;
    --teal-text: #1f8a80;
    --body-text: #4a4a4a;
    --paper: #ffffff;
    --photo-dark: #3a3d42;
    --photo-light: #d9c7b5;
  }
  html, body { margin: 0; padding: 0; overflow: hidden; }
  body { background: var(--paper); }
  .sheet {
    position: relative;
    width: 887px; height: 1200px;
    overflow: hidden;
    background: var(--paper);
    font-family: "PT Sans", sans-serif;
    color: var(--body-text);
  }
  .header-band { position: absolute; left: 0; top: 113px; width: 634px; height: 209px; background: var(--teal); }
  .header-edge { position: absolute; left: 838px; top: 113px; width: 49px; height: 209px; background: var(--teal); }
  .portrait {
    position: absolute; left: 634px; top: 113px; width: 204px; height: 228px;
    background: linear-gradient(180deg, var(--photo-light) 0%, #b89c86 45%, var(--photo-dark) 100%);
  }
  .brand { position: absolute; left: 60px; top: 178px; color: var(--paper); display: flex; align-items: center; gap: 14px; }
  .brand-dot { width: 44px; height: 44px; border-radius: 50%; background: var(--paper); flex: none; }
  .brand-name {
    font-family: "Crimson Text", serif; font-weight: 600;
    font-size: 38px; line-height: 1; letter-spacing: 0.5px;
    font-variant: small-caps; margin: 0;
  }
  .brand-role {
    font-family: "Crimson Text", serif; font-weight: 600;
    font-size: 13.5px; letter-spacing: 2.4px; text-transform: uppercase; margin: 4px 0 0;
  }
  .web { position: absolute; left: 218px; top: 287px; color: var(--paper); font-size: 18px; letter-spacing: 0.3px; }
  .section { position: absolute; left: 68px; }
  .section h2 {
    font-family: "Crimson Text", serif; font-weight: 400;
    font-size: 28px; color: var(--teal-text); margin: 0;
  }
  .bullets { list-style: none; margin: 0; padding: 0; font-size: 14.6px; }
  .bullets li { position: relative; padding-left: 25px; }
  .bullets li::before {
    content: ""; position: absolute; left: 1px; top: 50%;
    width: 12px; height: 12px; margin-top: -6px; border-radius: 50%; background: var(--teal);
  }
  .procedures { top: 436px; }
  .procedures .bullets { margin-top: 24px; }
  .procedures li { height: 23.5px; line-height: 23.5px; }
  .eligibility { top: 668px; }
  .eligibility .bullets { margin-top: 28px; }
  .eligibility li { height: 32px; line-height: 32px; }
  .locations { top: 817px; }
  .locations .bullets { margin-top: 32px; }
  .locations li { height: 28.5px; line-height: 28.5px; padding-left: 27px; }
  .note {
    position: absolute; left: 66px; top: 1003px; width: 770px; margin: 0;
    font-family: "Crimson Text", serif; font-size: 20.5px; line-height: 25px; color: var(--teal-text);
  }
  .footer-band { position: absolute; left: 0; top: 1166px; width: 887px; height: 34px; background: var(--teal); }
</style>
</head>
<body>
<div class="sheet">
  <div class="header-band"></div>
  <div class="header-edge"></div>
  <div class="portrait" role="img" aria-label="Headshot of the surgeon in a dark suit"></div>

  <div class="brand">
    <span class="brand-dot"></span>
    <div>
      <p class="brand-name">Marcus Belwether</p>
      <p class="brand-role">General, Upper GI &amp; Bariatric Surgeon</p>
    </div>
  </div>
  <div class="web">www.marcusbelwether.com.au</div>

  <section class="section procedures">
    <h2>Bariatric Surgery Procedures Offered</h2>
    <ul class="bullets">
      <li>Sleeve Gastrectomy</li>
      <li>Gastric Bypass</li>
      <li>Gastric Banding</li>
      <li>Revisional surgery</li>
      <li>Endoliner or Intra gastric balloon implantation</li>
      <li>Gastric Band Management. Abdominoplasty or Arm Reduction for weight loss patients.</li>
    </ul>
  </section>

  <section class="section eligibility">
    <h2>Standard Eligibility Criteria for Bariatric Surgery</h2>
    <ul class="bullets">
      <li>BMI &gt; 35 with diabetes or other obesity related co-morbidity</li>
      <li>BMI 30 – 35 selected cases</li>
    </ul>
  </section>

  <section class="section locations">
    <h2>Operating Locations</h2>
    <ul class="bullets">
      <li>Larkmont Eastern Hospital</li>
      <li>Larkmont Riverside Hospital</li>
      <li>Hollin Vale Public Hospital</li>
      <li>Southmere District Hospital, Alder Bay</li>
    </ul>
  </section>

  <p class="note">Please note that for sleeve gastrectomy &amp; gastric bypass procedures, Private health insurance of the appropriate level is mandatory to proceed with surgery.</p>

  <div class="footer-band"></div>
</div>
</body>
</html>
```